TAVRO Capital Group LLC a High Risk Big Rewards company for Rich Young Entrepreneurs

We would like a very modern, powerful in the eyes of our customers, modern, minimalist feel, financial gain. this business card is for young Rich entrepreneurs who want to invest money into High Risk, Big Rewards Businesses. The card Should sell the business!! let your creativity go Wild! I pick most of the designers for this project because of your BOLD Designs, I would like this card to be Bold, Modern, Minimalist, use as many effects in your graphic Artist Mind, Do not let the Financial sound of this business to make you think Conservative that's the last thing we are! if you have a lot of money and you want to play a risky market call US
Updates

Project Deadline Extended
Reason: have not received, enough designs to choose 1st and second place, sure I have received over 100 designs but it seems most designers are submitting every card they have ever made before and calling it mine, please we are looking for fresh ideas please!

Target Market(s)

Private Risky Investors

Industry/Entity Type

Financial

Contact Information for Business Card

powerful in the eyes of our customers,modern, minimalist feel

Font styles to use
Other font styles liked:
• Modern feeling fonts

Requirements
Must have
• The Company Name is TAVRO Capital Group LLC and it must be on the CARD
• My Name, title, Cell , email
• Delvin Ashcroft G.E.D.
• Managing Member
• 555.038.6195
• delvin@tavrocapitalgroup.example
Nice to have
• try a black thick plastic card with round corners with Delvin Ashcroft GED (make sure GED is smaller than name) just on one side of the card, and my phone number with out the icons and email on the other side, this card should look like a exclusive credit card or exclusive VIP card, something you would never loose

```html
<!DOCTYPE html>
<html lang="en">
<head>
<meta charset="utf-8">
<title>TAVRO Capital Group LLC — Business Card</title>
<link rel="stylesheet" href="https://fonts.googleapis.com/css2?family=Fira+Sans:wght@400;500;600;700&display=swap">
<style>
  :root {
    --sky: #43b6e8;
    --navy: #16416a;
    --ocean: #0a5a8c;
    --figure-light: #a9dcf4;
    --figure-gold: #f6b912;
    --figure-mid: #1576b4;
    --white: #ffffff;
    --page: #ffffff;
  }
  * { box-sizing: border-box; margin: 0; padding: 0; }
  html, body {
    width: 1200px; height: 1000px; overflow: hidden;
    background: var(--page);
    font-family: "Fira Sans", sans-serif;
  }
  .canvas { position: relative; width: 1200px; height: 1000px; }

  .card {
    position: absolute;
    width: 770px; height: 450px;
    overflow: hidden;
  }
  .card svg.art { position: absolute; inset: 0; }

  .card--front { left: 58px; top: 80px; background: var(--sky); z-index: 2; }
  .card--back  { left: 385px; top: 500px; width: 760px; height: 430px; background: var(--navy); z-index: 1; }

  .brand {
    position: absolute;
    display: flex; align-items: center; gap: 14px;
    color: var(--white);
    font-weight: 700;
    line-height: 1.05;
  }
  .brand__square { width: 22px; height: 22px; background: var(--navy); flex: none; }
  .card--back .brand__square { background: var(--white); }
  .brand__name { font-size: 40px; }
  .card--front .brand { left: 40px; top: 70px; width: 260px; }
  .card--back .brand { left: 265px; top: 150px; width: 260px; }

  .person { position: absolute; left: 372px; top: 218px; color: var(--white); }
  .person__name {
    font-size: 25px; font-weight: 500; letter-spacing: 1.5px;
    text-transform: uppercase; line-height: 1.2;
  }
  .person__name small { font-size: 0.78em; }
  .person__title {
    margin-top: 16px;
    font-size: 14px; font-weight: 600; letter-spacing: 1.6px;
    text-transform: uppercase;
  }
  .contact { margin-top: 34px; list-style: none; font-size: 18px; line-height: 1.55; }
  .contact li { display: flex; align-items: center; gap: 9px; }
  .contact svg { width: 18px; height: 18px; flex: none; }
</style>
</head>
<body>
<main class="canvas">

  <section class="card card--front" aria-label="Business card front">
    <svg class="art" width="770" height="450" viewBox="0 0 770 450">
      <rect class="runners" role="img" aria-label="Illustration: business people running up the stairs"
            x="250" y="10" width="210" height="300" fill="url(#runnerTone)"/>
      <path class="stairs" fill="var(--navy)"
            d="M0 450 V400 H75 V370 H120 V340 H165 V310 H210 V280 H255 V250 H300 V220 H345 V190 H390 V160 H435 V130 H480 V100 H525 V70 H570 V40 H615 V10 H660 V0 H770 V450 Z"/>
      <defs>
        <linearGradient id="runnerTone" x1="0" y1="0" x2="1" y2="0">
          <stop offset="0" stop-color="#ffffff" stop-opacity="0.85"/>
          <stop offset="0.5" stop-color="#f6b912" stop-opacity="0.85"/>
          <stop offset="1" stop-color="#a9dcf4" stop-opacity="0.85"/>
        </linearGradient>
      </defs>
    </svg>

    <div class="brand">
      <span class="brand__square"></span>
      <span class="brand__name">TAVRO Capital Group LLC</span>
    </div>

    <div class="person">
      <h1 class="person__name">Delvin<br>Ashcroft <small>G.E.D.</small></h1>
      <p class="person__title">Managing Member</p>
      <ul class="contact">
        <li>
          <svg viewBox="0 0 24 24" aria-hidden="true"><path fill="#fff" d="M6.6 10.8c1.4 2.8 3.8 5.1 6.6 6.6l2.2-2.2c.3-.3.7-.4 1-.2 1.1.4 2.3.6 3.6.6.6 0 1 .4 1 1V20c0 .6-.4 1-1 1C10.6 21 3 13.4 3 4c0-.6.4-1 1-1h3.5c.6 0 1 .4 1 1 0 1.3.2 2.5.6 3.6.1.3 0 .7-.2 1z"/></svg>
          <span>555.038.6195</span>
        </li>
        <li>
          <svg viewBox="0 0 24 24" aria-hidden="true"><rect x="2.5" y="5.5" width="19" height="13" fill="none" stroke="#fff" stroke-width="2"/><path d="M3 6l9 7 9-7" fill="none" stroke="#fff" stroke-width="2"/></svg>
          <span>delvin@tavrocapitalgroup.example</span>
        </li>
      </ul>
    </div>
  </section>

  <section class="card card--back" aria-label="Business card back">
    <svg class="art" width="760" height="430" viewBox="0 0 760 430">
      <path class="stairs" fill="var(--ocean)"
            d="M90 0 H760 V430 H700 V400 H660 V370 H620 V340 H580 V310 H540 V280 H500 V250 H460 V220 H420 V190 H380 V160 H340 V130 H300 V100 H260 V70 H210 V40 H150 V15 H90 Z"/>
      <rect class="runners" role="img" aria-label="Illustration: business people climbing the stairs"
            x="290" y="25" width="430" height="360" fill="var(--figure-mid)" opacity="0.55"/>
    </svg>

    <div class="brand">
      <span class="brand__square"></span>
      <span class="brand__name">TAVRO Capital Group LLC</span>
    </div>
  </section>

</main>
</body>
</html>
```